Need Beautiful Banners for On-Site Marketing

Hello,
We are looking to create some banners for use on our site to highlight some features of our business. Our inspiration for these banners and their placement comes from the design on http://www.vendrick.com. We like their marketing banners and would like to create something along these lines.
I've uploaded two files to show exactly how and where these banners will be fitting into our design. **Disregard the Blue color used in the example files** Also, the larger banner ad in the uploaded files is incorrect height. Refer below for sizes.
There are two sizes for the banners:
1. Small - 475px Width and Approx. 45px Height. Seen under the header on our site.
2. Large - 960px Width and Approx. 45px height. These will be used in the content portions of the site and spread across width of page.
5 Banners needed with the following details:
1. (Small) - First Time Buyer Discount - 5% - Use checkout code "Open5".
This banner will not be a link, so no need for a button or arrow signifying link.
2. (Small). Larger Orders? No problem! Save Time and Money Today. Get a Quote Now.
This banner will be linked to a quote page.
3. (Large) We are Halvorcast Commercial Specialist! - Expert Service, Lower Pricing, Larger Catalog, More Replacement Parts.
This banner will be linked to our "about-us" page.
4. (Large) $65 million+ Inventory Across 31 Distribution Centers. Larger Catalog, Lower Prices, Fast 1-2 Day Shipping.
This banner will be linked to our shipping page.
5. (Large) Introducing our State-of-the-Art Inventory Tool:
Check Live local stock levels at 31 Nationwide Distribution Centers Today!
This will be linked to an informational page.
So.. 2 Small and 3 Large Banners. All text in these banners can be edited how you see fit. We'd like to have at least some continuity across the designs for all banners. If you look at vendrick.com, they use the same skinny text and link button graphics in most of their banners.
Thanks!! Looking forward to these designs!
Reason: Really need something more for 5 banners.. Anyone?

```html
<!DOCTYPE html>
<html lang="en">
<head>
<meta charset="utf-8">
<title>Larger Orders Banner</title>
<link rel="stylesheet" href="https://fonts.googleapis.com/css2?family=Archivo+Black&family=Open+Sans:ital,wght@1,800&family=Roboto+Condensed:ital,wght@0,400;1,400;1,500&display=swap">
<style>
  :root {
    --page: #ffffff;
    --carbon-dark: #151515;
    --carbon-mid: #262626;
    --red-bright: #c00d0d;
    --red-deep: #7d0202;
    --ink-dark: #2a2a2a;
    --text-light: #ffffff;
    --button-top: #d01414;
    --button-bottom: #8a0303;
    --button-edge: #5a0000;
  }
  html, body {
    margin: 0;
    width: 1200px;
    height: 900px;
    overflow: hidden;
    background: var(--page);
  }
  .quote-banner {
    position: absolute;
    left: 126px;
    top: 414px;
    width: 950px;
    height: 88px;
    border-radius: 8px;
    overflow: hidden;
    background: linear-gradient(180deg, var(--carbon-mid) 0%, var(--carbon-dark) 100%);
    box-shadow: 0 0 0 1px #0b0b0b;
  }
  .quote-banner__red-band {
    position: absolute;
    left: 0;
    top: 0;
  }
  .quote-banner__headline {
    position: absolute;
    left: 14px;
    top: 4px;
    margin: 0;
    font-family: "Open Sans", sans-serif;
    font-style: italic;
    font-weight: 800;
    font-size: 37px;
    line-height: 44px;
    letter-spacing: 0.5px;
    color: var(--text-light);
    white-space: nowrap;
  }
  .quote-banner__subline {
    position: absolute;
    left: 44px;
    top: 44px;
    margin: 0;
    font-family: "Archivo Black", sans-serif;
    font-size: 33px;
    line-height: 40px;
    color: var(--ink-dark);
    white-space: nowrap;
  }
  .quote-banner__pitch {
    position: absolute;
    left: 412px;
    top: 6px;
    width: 230px;
    margin: 0;
    font-family: "Roboto Condensed", sans-serif;
    font-style: italic;
    font-weight: 400;
    font-size: 31px;
    line-height: 37px;
    letter-spacing: 2px;
    text-align: center;
    color: var(--text-light);
    white-space: nowrap;
  }
  .quote-banner__button {
    position: absolute;
    left: 660px;
    top: 14px;
    width: 270px;
    height: 62px;
    border-radius: 5px;
    background: linear-gradient(180deg, var(--button-top) 0%, var(--red-bright) 45%, var(--button-bottom) 100%);
    border: 1px solid var(--button-edge);
    box-sizing: border-box;
    display: flex;
    align-items: center;
    justify-content: center;
    font-family: "Roboto Condensed", sans-serif;
    font-style: italic;
    font-weight: 500;
    font-size: 37px;
    color: var(--text-light);
    text-decoration: none;
    white-space: nowrap;
  }
</style>
</head>
<body>
  <section class="quote-banner">
    <svg class="quote-banner__red-band" width="400" height="88" viewBox="0 0 400 88" aria-hidden="true">
      <defs>
        <linearGradient id="redBandFill" x1="0" y1="0" x2="0" y2="1">
          <stop offset="0" stop-color="#c80f0f"/>
          <stop offset="1" stop-color="#6e0202"/>
        </linearGradient>
      </defs>
      <polygon points="0,0 392,0 326,88 0,88" fill="url(#redBandFill)"/>
    </svg>
    <h2 class="quote-banner__headline">LARGER ORDERS?</h2>
    <p class="quote-banner__subline">NO PROBLEM!</p>
    <p class="quote-banner__pitch">SAVE TIME AND<br>MONEY TODAY</p>
    <a class="quote-banner__button" href="#quote">Get a Quote Now</a>
  </section>
</body>
</html>
```